Business Management Fortress

Assist with enhancing a powerpoint slide by providing a few design options for consideration. I have a template but open to any creative ideas.

Target Market(s)

Internal employees and stakeholders

Industry/Entity Type

Business Management, Finance, Accounting

Requirements
Must have
• Maintain a fortress, temple, or pyramid schema
Nice to have
• Scenic Background

```html
<!DOCTYPE html>
<html lang="en">
<head>
<meta charset="utf-8">
<title>Business Management Fortress</title>
<link href="https://fonts.googleapis.com/css2?family=Figtree:wght@400;500;700&display=swap" rel="stylesheet">
<style>
  :root {
    --bg: #ffffff;
    --stone: #dae3f3;
    --stone-dark: #d0dbea;
    --stone-shadow: #b8c7e8;
    --ink: #111111;
    --blue: #4a9cf6;
    --orange: #f7ae3b;
    --green: #3dbd84;
    --red: #fb2f4e;
    --white: #ffffff;
  }
  html, body { margin: 0; padding: 0; overflow: hidden; background: var(--bg); }
  .fortress { display: block; width: 1200px; height: 675px; font-family: "Figtree", sans-serif; }
  .stone { fill: var(--stone); }
  .stone-dark { fill: var(--stone-dark); }
  .stone-shadow { fill: var(--stone-shadow); }
  .medallion { fill: var(--white); }
  .leader-line { fill: none; stroke: var(--ink); stroke-width: 3; }
  .leader-dot { fill: var(--ink); }
  .value-label { font-size: 42px; font-weight: 400; }
  .value-label--leaders { fill: var(--orange); }
  .value-label--partner { fill: var(--blue); }
  .value-label--profit { fill: var(--green); }
  .pillar-name { font-size: 48px; font-weight: 500; fill: var(--ink); }
  .base-title { font-size: 35px; font-weight: 700; fill: var(--ink); }
  .chip { fill: var(--white); }
  .chip-text { font-size: 26px; fill: var(--blue); }
  .fill-blue { fill: var(--blue); }
  .fill-orange { fill: var(--orange); }
  .fill-green { fill: var(--green); }
  .fill-red { fill: var(--red); }
</style>
</head>
<body>
<svg class="fortress" viewBox="0 0 2560 1440" xmlns="http://www.w3.org/2000/svg">
  <!-- Roof -->
  <g class="roof">
    <path class="stone" d="M1250 172 Q1280 160 1310 172 L1895 410 Q1912 418 1910 428 Q1908 442 1890 442 L670 442 Q652 442 650 428 Q648 418 665 410 Z"/>
    <path fill="var(--white)" d="M1043 255 L1055 250 L1245 442 L1230 442 Z"/>
    <path fill="var(--white)" d="M1508 250 L1520 255 L1330 442 L1315 442 Z"/>
    <path class="stone" d="M712 442 H1850 V475 Q1850 500 1825 500 H737 Q712 500 712 475 Z"/>
    <rect class="stone-shadow" x="712" y="442" width="1138" height="18"/>

    <circle class="medallion" cx="1013" cy="358" r="70"/>
    <circle class="fill-orange" cx="1013" cy="358" r="38" role="img" aria-label="Leaders icon"/>
    <circle class="medallion" cx="1280" cy="305" r="70"/>
    <circle class="fill-blue" cx="1280" cy="305" r="38" role="img" aria-label="Partnership handshake icon"/>
    <circle class="medallion" cx="1548" cy="358" r="70"/>
    <circle class="fill-green" cx="1548" cy="358" r="38" role="img" aria-label="Money bag in hand icon"/>

    <path class="leader-line" d="M880 203 H975 Q1013 203 1013 241 V288"/>
    <circle class="leader-dot" cx="1013" cy="288" r="6"/>
    <path class="leader-line" d="M1280 130 V235"/>
    <circle class="leader-dot" cx="1280" cy="235" r="6"/>
    <path class="leader-line" d="M1685 203 H1590 Q1550 203 1550 241 V288"/>
    <circle class="leader-dot" cx="1550" cy="288" r="6"/>

    <text class="value-label value-label--leaders" x="787" y="215" text-anchor="middle">Leaders</text>
    <text class="value-label value-label--partner" x="1280" y="108" text-anchor="middle">Partner</text>
    <text class="value-label value-label--profit" x="1815" y="215" text-anchor="middle">Profitability</text>
  </g>

  <!-- Pillars -->
  <defs>
    <g id="pillar-body">
      <rect class="stone-dark" x="-77" y="527" width="154" height="32" rx="16"/>
      <path class="stone" d="M-57 559 H57 Q75 700 76 900 L76 1000 L-76 1000 L-76 900 Q-75 700 -57 559 Z"/>
      <path class="stone-shadow" d="M-62 1080 H62 L57 1140 H-57 Z"/>
      <path class="stone" d="M-55 1100 H55 L57 1140 H-57 Z"/>
      <circle class="stone" cx="0" cy="995" r="115"/>
      <path class="stone-shadow" d="M-60 1100 Q0 1135 60 1100 L60 1112 Q0 1145 -60 1112 Z"/>
      <rect class="stone-dark" x="-77" y="1140" width="154" height="32" rx="16"/>
    </g>
  </defs>

  <g class="pillar" transform="translate(857 0)">
    <use href="#pillar-body"/>
    <path class="fill-blue" d="M-25 560 H25 L0 600 Z"/>
    <circle class="fill-blue" cx="0" cy="995" r="86" role="img" aria-label="People icon"/>
    <text class="pillar-name" transform="translate(16 880) rotate(-90)">People</text>
  </g>
  <g class="pillar" transform="translate(1140 0)">
    <use href="#pillar-body"/>
    <path class="fill-orange" d="M-25 560 H25 L0 600 Z"/>
    <circle class="fill-orange" cx="0" cy="995" r="86" role="img" aria-label="Innovation lightbulb icon"/>
    <text class="pillar-name" transform="translate(16 880) rotate(-90)">Innovation</text>
  </g>
  <g class="pillar" transform="translate(1422 0)">
    <use href="#pillar-body"/>
    <path class="fill-green" d="M-25 560 H25 L0 600 Z"/>
    <circle class="fill-green" cx="0" cy="995" r="86" role="img" aria-label="Business intelligence brain icon"/>
    <text class="pillar-name" transform="translate(-6 880) rotate(-90)">Business</text>
    <text class="pillar-name" transform="translate(38 880) rotate(-90)">Intelligence</text>
  </g>
  <g class="pillar" transform="translate(1705 0)">
    <use href="#pillar-body"/>
    <path class="fill-red" d="M-25 560 H25 L0 600 Z"/>
    <circle class="fill-red" cx="0" cy="995" r="86" role="img" aria-label="Strategic alliances icon"/>
    <text class="pillar-name" transform="translate(-6 880) rotate(-90)">Strategic</text>
    <text class="pillar-name" transform="translate(38 880) rotate(-90)">Alliances</text>
  </g>

  <!-- Foundation -->
  <g class="foundation">
    <path class="stone" d="M733 1260 V1225 Q733 1195 763 1195 H1798 Q1828 1195 1828 1225 V1260 Z"/>
    <rect class="stone" x="652" y="1253" width="1258" height="137" rx="24"/>
    <text class="base-title" x="1280" y="1248" text-anchor="middle">Fiduciary Responsibilities</text>

    <rect class="chip" x="918" y="1278" width="246" height="40" rx="8"/>
    <text class="chip-text" x="1041" y="1307" text-anchor="middle">Accurate Financials</text>
    <rect class="chip" x="1181" y="1278" width="222" height="40" rx="8"/>
    <text class="chip-text" x="1292" y="1307" text-anchor="middle">Internal Controls</text>
    <rect class="chip" x="1420" y="1278" width="222" height="40" rx="8"/>
    <text class="chip-text" x="1531" y="1307" text-anchor="middle">Brand Protection</text>

    <rect class="chip" x="1018" y="1334" width="160" height="40" rx="8"/>
    <text class="chip-text" x="1098" y="1363" text-anchor="middle">Compliance</text>
    <rect class="chip" x="1194" y="1334" width="96" height="40" rx="8"/>
    <text class="chip-text" x="1242" y="1363" text-anchor="middle">Ethics</text>
    <rect class="chip" x="1306" y="1334" width="237" height="40" rx="8"/>
    <text class="chip-text" x="1424" y="1363" text-anchor="middle">Cost Management</text>
  </g>
</svg>
</body>
</html>
```